Web design for our new company

We need a web design for our product and for our company.
And the main is our Product tool called "velmora".
----------------------------------------------------------
[Our company's Goal]
Make organization’s communication smooth and healthy with transparency and efficiency for works and tasks in all levels with our workflow tool.

[Our Mission]
Our mission is to achieve business goals with customers.
We work together to identify the goals for your company, guides your strategy and bring the technology answers which best fit to achieve the goals.

[What we do]
We have a workflow tool "velmora"
- Very simple end-user configurable workflow for any company processes
(Targeting small-med size company)
- Graphical & fun features for startup users
- Simple and easy task control with quillbox e-mail look & feel
- Non charged skill up guidance
- Additional features with;
Multiple delegation
Clear status for each owner
Task owner management console with due date reminders&reporting

Others
1. System Development & Implementation Service
Our client list includes a wide variety of small to medium to major sized enterprises.
We can offer from full-scratch based development to packaged system implementation.

2. Project Management(PM) Service
We will provide end-to-end PM service with experienced PM.
Our service is not only “managing” but “leading” to bring success to achieve the goal.

3.Consultation Service

Consulting services to a wide range of fields such as creating business strategy, business process Kaizen, IT system consultation and change management.

Target Market(s)

Business to Business
Mainly to medium size - startup company

Industry/Entity Type

It Company

Coding

Coded - Design and coding required

Number of Pages Required

5+ page

Colors
0255a3
33a6d7
86cfc6
33b8a4
add136
cadf82
fbf289
fee18a
faa54b

Requirements
Must have
• We need Pages for
• Company mission
• Service Overview
• Contact
• Privacy Policy
• Terms and Conditions
• =========================
• As there were some questions, I add followings.---------
• 1. File Format
• We are going to use Brixel cloud services to upload finished web files.
• The finished files should be ready to use by simply replacing images and text.
• Please provide me "easy to handle" template with "sophisticated design".
• Thanks!
• 2. Multiple Languages
• We need buttons for changing language.
• We will have this translated to German, English and Japanese.
• Thank you so much!!
Nice to have
• These are current Logos and will be a next project to revise them...
• Attached Company Profile and Logo design
• 1. Company Profile
• 2. Our Company Logo
• 3. Our Product Logo -> This is most close to our image of design base.
• 4. Product Logo for PPT Header
• All just for your reference.
• ---------
• As there were some request, I added attachment as for contents for Our mission page.
Should not have
• I hope to see some unique designs.
• (Sorry please ignore my last update as I checked with our CEO.
• Bootstrap is absolutely good template.)

```html
<!DOCTYPE html>
<html lang="en">
<head>
<meta charset="utf-8">
<title>KORVEN E.U. – IT Consulting and System Development</title>
<link rel="stylesheet" href="https://fonts.googleapis.com/css2?family=Open+Sans:wght@300;400;600;700&display=swap">
<style>
:root{
  --green:#8aab3a;
  --green-light:#a8c84a;
  --green-deep:#6f8f2a;
  --ink:#333333;
  --muted:#666666;
  --white:#ffffff;
  --blush:#faf5f3;
  --footer:#e9e9e9;
  --phone:#f7f7f7;
  --badge:#111111;
}
*{box-sizing:border-box;margin:0;padding:0}
html,body{width:1200px;height:2857px;overflow:hidden}
body{font-family:"Open Sans",Arial,sans-serif;color:var(--ink);background:var(--white);position:relative}
section,header,footer{position:absolute;left:0;width:1200px}
.abs{position:absolute}
a{text-decoration:none;color:inherit}

/* hero */
.hero{top:0;height:682px;background:linear-gradient(120deg,#3b4246 0%,#2b3134 45%,#3c4549 100%)}
.hero-photo{position:absolute;inset:0;background:radial-gradient(ellipse at 25% 55%,rgba(150,120,110,.35),transparent 45%),radial-gradient(ellipse at 75% 25%,rgba(90,110,120,.35),transparent 50%)}
.brand{left:108px;top:150px;display:flex;align-items:center;gap:12px;color:var(--green);font-weight:600;font-size:30px;letter-spacing:2px}
.brand-dot{width:26px;height:26px;border-radius:50%;background:var(--green)}
.nav a{position:absolute;top:70px;font-size:12px;font-weight:600;color:var(--white);white-space:nowrap}
.nav a.active{color:var(--green-light)}
.lang{top:28px;right:109px;display:flex;gap:6px;font-size:11px;font-weight:600;color:var(--white)}
.lang a{padding:2px 6px;border:1px solid rgba(255,255,255,.5);border-radius:2px}
.lang a.current{background:var(--green);border-color:var(--green)}
.hero-title{top:372px;width:1200px;text-align:center;font-size:39px;font-weight:400;color:var(--white);letter-spacing:.3px}
.hero-sub{top:434px;width:1200px;text-align:center;font-size:12.5px;font-weight:600;color:var(--white);line-height:20px}
.btn{display:inline-flex;align-items:center;justify-content:center;font-size:14px;font-weight:600;color:var(--white);text-transform:uppercase;border-radius:2px}
.btn-outline{left:442px;top:497px;width:143px;height:35px;border:1.5px solid var(--white)}
.btn-fill{left:596px;top:497px;width:160px;height:35px;background:var(--green)}
.arrow{top:305px}

/* welcome */
.welcome{top:682px;height:246px;text-align:center}
.section-title{font-size:31px;font-weight:300;color:var(--ink);letter-spacing:.5px}
.section-title span{color:var(--green)}
.welcome .section-title{margin-top:66px}
.welcome p{width:842px;margin:16px auto 0;font-size:11px;line-height:21px;color:var(--muted)}

/* mission */
.mission{top:928px;height:476px;background:repeating-linear-gradient(90deg,#e6e6e6 0 38px,#ececec 38px 76px,#e2e2e2 76px 115px)}
.phone{top:66px;width:160px;height:339px;border-radius:24px;background:var(--phone);border:1px solid #d4d4d4;box-shadow:0 4px 10px rgba(0,0,0,.12)}
.phone-left{left:223px}
.phone-right{left:335px;box-shadow:-4px 4px 12px rgba(0,0,0,.15)}
.phone-speaker{left:58px;top:22px;width:44px;height:4px;border-radius:2px;background:#c9c9c9}
.phone-home{left:64px;top:300px;width:30px;height:30px;border-radius:50%;border:1.5px solid #c9c9c9}
.screen{left:10px;top:44px;width:138px;height:244px}
.screen-green{background:linear-gradient(180deg,#93b13f,#86a536)}
.screen-target{background:linear-gradient(180deg,#9ab848 0%,#9ab848 20%,#eeeeee 20%,#e2e2e2 100%)}
.mission-title{left:549px;top:84px;font-size:38px;font-weight:300}
.mission-sub{left:549px;top:136px;font-size:19px;color:var(--ink)}
.mission-copy{left:549px;top:180px;width:520px;font-size:10.5px;line-height:21px;color:var(--ink)}
.checks{left:549px;top:281px;font-size:10.5px;line-height:23px;list-style:none}
.checks li{display:flex;align-items:center;gap:10px}
.checks li::before{content:"";width:10px;height:10px;border:1.5px solid var(--ink);background:linear-gradient(var(--ink),var(--ink)) center/5px 5px no-repeat}
.store{top:346px;width:131px;height:40px;border-radius:6px;background:var(--badge);border:1px solid #555;display:flex;align-items:center;gap:10px;padding-left:12px}
.store-a{left:547px}.store-b{left:690px}
.store-mark{width:20px;height:20px;border-radius:50%;background:var(--white)}
.store-lines{display:flex;flex-direction:column;gap:5px}
.store-lines i{display:block;height:3px;border-radius:2px;background:#bbbbbb;width:46px}
.store-lines i+i{height:6px;width:70px;background:var(--white)}

/* services */
.services{top:1404px;height:310px;background:var(--blush)}
.services .section-title{position:absolute;top:50px;width:1200px;text-align:center;font-size:30px}
.service{top:120px;width:320px;height:170px}
.service svg{position:absolute;left:0;top:4px}
.service h3{position:absolute;top:0;font-size:14px;font-weight:400;line-height:23px;color:var(--ink)}
.service p{position:absolute;top:62px;width:200px;font-size:10.5px;line-height:21px;color:var(--muted)}
.service .more{position:absolute;top:141px;font-size:10.5px;color:var(--ink);text-transform:uppercase}
.s1{left:104px}.s1 h3,.s1 p,.s1 .more{left:85px}
.s2{left:450px}.s2 h3,.s2 p,.s2 .more{left:97px}
.s3{left:820px}.s3 h3,.s3 p,.s3 .more{left:79px}
.s3 p{top:44px}.s3 .more{top:131px}

/* ceo */
.ceo{top:1714px;height:395px}
.video{left:99px;top:60px;width:465px;height:261px;background:linear-gradient(180deg,#d8d8d4,#bfbfba);box-shadow:0 0 0 4px #f0f0f0}
.video-play{left:312px;top:172px;width:52px;height:34px;border-radius:8px;background:rgba(60,60,60,.75)}
.video-play::after{content:"";position:absolute;left:21px;top:10px;border-left:13px solid var(--white);border-top:7px solid transparent;border-bottom:7px solid transparent}
.ceo-title{left:596px;top:58px;font-size:30px;font-weight:300}
.ceo-copy{left:596px;top:107px;width:508px;font-size:10.3px;line-height:20px;color:var(--ink)}
.ceo-copy p+p{margin-top:9px}
.ceo-sign{right:99px;top:284px;text-align:right;font-size:10.3px;line-height:20px}
.ceo-btn{left:596px;top:307px;width:105px;height:31px;background:var(--green);font-size:12px}

/* product */
.product{top:2109px;height:365px;background:linear-gradient(180deg,#3a3d3f,#262829);color:var(--white);text-align:center}
.product-photo{position:absolute;inset:0;background:radial-gradient(ellipse at 68% 30%,rgba(120,120,120,.35),transparent 40%)}
.product h2{position:absolute;top:96px;width:1200px;font-size:28px;font-weight:700}
.product p{position:absolute;top:152px;left:190px;width:820px;font-size:10.3px;line-height:20px}
.product-name{top:251px;left:0;width:1200px;display:flex;justify-content:center;align-items:center;gap:10px;font-size:28px;font-weight:600}
.product-name i{width:22px;height:22px;background:var(--white)}

/* newsletter */
.newsletter{top:2474px;height:155px}
.news-title{left:253px;top:62px;font-size:22px;font-weight:400}
.news-sub{left:253px;top:96px;font-size:15px;color:var(--muted)}
.news-input{left:549px;top:69px;width:310px;height:44px;border:1px solid #ddd;font-size:11px;color:#999;padding:14px 10px}
.news-btn{left:859px;top:69px;width:128px;height:44px;background:var(--green);font-size:14px}

/* footer */
.footer{top:2629px;height:228px}
.socials{top:112px;left:514px;display:flex;gap:8px}
.socials i{width:28px;height:28px;border-radius:50%;background:#9a9a9a}
.links{top:155px;width:1200px;text-align:center;font-size:9.5px;color:var(--ink)}
.links span{margin:0 5px}
.copy{top:182px;width:1200px;text-align:center;font-size:9.5px;color:var(--ink)}
</style>
</head>
<body>

<header class="hero">
  <div class="hero-photo" role="img" aria-label="Photo of a businesswoman holding a laptop, with floating device and cloud icons"></div>
  <div class="abs brand"><span class="brand-dot"></span>KORVEN</div>
  <div class="abs lang"><a class="current">EN</a><a>DE</a><a>JA</a></div>
  <nav class="nav">
    <a class="active" style="left:524px">HOME</a>
    <a style="left:592px">ABOUT US</a>
    <a style="left:684px">COMPANY MISSION</a>
    <a style="left:823px">SERVICE OVERVIEW</a>
    <a style="left:960px">PRODUCTS</a>
    <a style="left:1034px">CONTACT</a>
  </nav>
  <svg class="abs arrow" style="left:36px" width="32" height="60" viewBox="0 0 32 60"><path d="M28 2 L4 30 L28 58" fill="none" stroke="#fff" stroke-width="2"/></svg>
  <svg class="abs arrow" style="left:1132px" width="32" height="60" viewBox="0 0 32 60"><path d="M4 2 L28 30 L4 58" fill="none" stroke="#fff" stroke-width="2"/></svg>
  <h1 class="abs hero-title">IT CONSULTING AND SYSTEM DEVELOPMENT</h1>
  <p class="abs hero-sub">Make organization’s communication smooth and healthy with transparency and efficiency<br>for works and tasks in all levels with our workflow tool.</p>
  <a class="abs btn btn-outline">Learn More</a>
  <a class="abs btn btn-fill">Get Started</a>
</header>

<section class="welcome">
  <h2 class="section-title">WELCOME TO <span>KORVEN E.U.</span></h2>
  <p>Make organization’s communication smooth and healthy with transparency and efficiency for works and tasks in all levels with our workflow tool. Our mission is to achieve business goals with customers. We work together to identify the goals for your company, guides your strategy and bring the technology answers which best fit to achieve the goals.</p>
</section>

<section class="mission">
  <div class="abs phone phone-left">
    <span class="abs phone-speaker"></span>
    <div class="abs screen screen-green" role="img" aria-label="App screen with an illustration of a team looking ahead"></div>
    <span class="abs phone-home"></span>
  </div>
  <div class="abs phone phone-right">
    <span class="abs phone-speaker"></span>
    <div class="abs screen screen-target" role="img" aria-label="App screen with an illustration of a target"></div>
    <span class="abs phone-home"></span>
  </div>
  <h2 class="abs mission-title">OUR MISSION</h2>
  <p class="abs mission-sub">IT Consulting and System development</p>
  <p class="abs mission-copy">Our mission is to achieve business goals with customers.<br>We work together to identify the goals for your company, guides your strategy and bring the technology answers which best fit to achieve the goals, guides your strategy and bring technology answers which best fit to achieve the goals.</p>
  <ul class="abs checks">
    <li>Our mission is to achieve business goals with customers.</li>
    <li>We work together to identify the goals for your company.</li>
  </ul>
  <a class="abs store store-a" aria-label="Download the app"><span class="store-mark"></span><span class="store-lines"><i></i><i></i></span></a>
  <a class="abs store store-b" aria-label="Get the app"><span class="store-mark"></span><span class="store-lines"><i></i><i></i></span></a>
</section>

<section class="services">
  <h2 class="section-title">WHAT WE <span>DO</span></h2>
  <div class="abs service s1">
    <svg width="70" height="70" viewBox="0 0 70 70"><circle cx="35" cy="35" r="26" fill="none" stroke="#6f8f2a" stroke-width="6" stroke-dasharray="30 11"/><circle cx="35" cy="35" r="9" fill="#333"/></svg>
    <h3>Project Management<br>(PM) Service</h3>
    <p>We will provide end-to-end PM service with experienced PM. Our service is not only managing...</p>
    <span class="more">Read more ➞</span>
  </div>
  <div class="abs service s2">
    <svg width="70" height="70" viewBox="0 0 70 70"><path d="M10 10 L60 60 M60 10 L10 60" stroke="#6f8f2a" stroke-width="9" stroke-linecap="round"/><circle cx="35" cy="35" r="6" fill="#333"/></svg>
    <h3>System Development &amp;<br>Implementation Service</h3>
    <p>Our client list includes a wide variety of small to medium to major sized enterprises...</p>
    <span class="more">Read more ➞</span>
  </div>
  <div class="abs service s3">
    <svg width="70" height="70" viewBox="0 0 70 70"><circle cx="22" cy="18" r="9" fill="#6f8f2a"/><path d="M6 52 Q6 32 22 32 Q38 32 38 52 Z" fill="#6f8f2a"/><circle cx="50" cy="42" r="12" fill="none" stroke="#333" stroke-width="5"/></svg>
    <h3>Consultation Service</h3>
    <p>Consulting services to a wide range of fields such as creating business strategy...</p>
    <span class="more">Read more ➞</span>
  </div>
</section>

<section class="ceo">
  <div class="abs video" role="img" aria-label="Video still of the CEO in a dark suit"></div>
  <span class="abs video-play"></span>
  <h2 class="abs ceo-title section-title">OUR <span>CEO</span></h2>
  <div class="abs ceo-copy">
    <p>Lukas Brenner is the founder and CEO of KORVEN E.U. serving over 350 unique users monthly. Prior to founding KORVEN E.U. in 2013, Lukas held senior technical lead positions in Alder Network GmbH. He is a graduate of the Higher Technical College (Höhere Technische Lehranstalt) which is an engineering-focused school where he developed his first technical skills.</p>
    <p>“I believe the keys of successful business includes - building trust, capability or skills, creativity and yet needs strength and patience to overcome changes and continue to produce. These are our Core Values which reinforce the commitment – Integrity, Focus on Value Creation, Accountability, Simplicity, Flexibility and Passion.</p>
  </div>
  <div class="abs ceo-sign">KORVEN E.U.<br>C.E.O. ING. LUKAS BRENNER</div>
  <a class="abs btn ceo-btn">Read More</a>
</section>

<section class="product">
  <div class="product-photo" role="img" aria-label="Photo of a hand using an online shop on a smartphone"></div>
  <h2>OUR PRODUCT</h2>
  <p>Our mission is to achieve business goals with customers. We work together to identify the goals for your company, guides your strategy and bring the technology answers which best fit to achieve the goals. I love challenges and working with people to find creative solutions. And I hope to find a solution for everyone.”<br>These are our Core Values which reinforce the commitment – Integrity, Focus on Value Creation, Accountability, Simplicity, Flexibility and Passion.</p>
  <div class="abs product-name"><i></i>velmora</div>
</section>

<section class="newsletter">
  <h3 class="abs news-title">Join our Newsletter.</h3>
  <p class="abs news-sub">Stay up to date with the latest news.</p>
  <div class="abs news-input">Name</div>
  <a class="abs btn news-btn">Subscribe</a>
</section>

<footer class="footer">
  <svg class="abs" style="left:0;top:0" width="1200" height="228" viewBox="0 0 1200 228"><rect width="1200" height="228" fill="#e9e9e9"/><polygon points="0,0 1200,0 600,72" fill="#ffffff"/></svg>
  <div class="abs socials"><i></i><i></i><i></i><i></i><i></i></div>
  <div class="abs links">HOME <span>/</span> COMPANY MISSION <span>/</span> SERVICE OVERVIEW <span>/</span> CONTACT <span>/</span> PRIVACY POLICY <span>/</span> TERMS AND CONDITIONS</div>
  <div class="abs copy">2018 © Copyrights All Rights Reserved</div>
</footer>

</body>
</html>
```